Business Card Design for a Personal Trainer

I need a business card design for my job as a personal trainer. It should have a unique, modern and exclusive design. On the front there should be only my logo with my name and my job. 0163/2918374 Tobias Kellinger Lindenfeldweg 14 80412 Munich Germany The most important contact information is the web adress. it can be bigger than the rest, but its not necessary. The card should be 8,5cmx5,5cm big. Font: Roboto. Colors: black, white, gray, 56c1ff.

```html
<!DOCTYPE html>
<html lang="de">
<head>
<meta charset="utf-8">
<title>Tobias Kellinger – Visitenkarte</title>
<link rel="stylesheet" href="https://fonts.googleapis.com/css2?family=Roboto:ital,wght@0,400;0,500;0,700;1,500&display=swap">
<style>
  :root {
    --accent: #5db9e8;
    --ink: #111111;
    --black: #000000;
    --white: #ffffff;
    --page: #ffffff;
    --photo-dark: #3a3a3a;
    --photo-light: #d9d9d9;
  }
  * { box-sizing: border-box; margin: 0; padding: 0; }
  html, body {
    width: 1200px; height: 1200px; overflow: hidden;
    background: var(--page);
    font-family: "Roboto", sans-serif;
  }
  .canvas { position: relative; width: 1200px; height: 1200px; }

  .card {
    position: absolute; left: 288px; width: 624px; height: 404px;
    box-shadow: 0 3px 10px rgba(0,0,0,0.28);
  }

  /* Contact side */
  .card--contact { top: 136px; background: var(--white); }
  .portrait {
    position: absolute; left: 42px; top: 34px; width: 155px; height: 155px;
    border: 3px solid var(--accent);
    background: var(--white);
    padding: 3px;
  }
  .portrait__fill {
    width: 100%; height: 100%;
    background: radial-gradient(ellipse at 50% 35%, var(--photo-light) 0%, #9a9a9a 45%, var(--photo-dark) 100%);
  }
  .name {
    position: absolute; right: 62px; top: 36px;
    font-weight: 700; font-size: 45px; letter-spacing: -0.3px;
    color: var(--accent); line-height: 1;
  }
  .website {
    position: absolute; right: 67px; top: 190px;
    font-weight: 500; font-style: italic; font-size: 19.5px;
    color: var(--ink); line-height: 1;
  }
  .divider { position: absolute; left: 27px; top: 227px; }
  .contact-list { position: absolute; left: 42px; top: 264px; list-style: none; }
  .contact-list li {
    position: relative; padding-left: 27px;
    font-size: 15.5px; line-height: 18.5px; color: var(--ink);
    margin-bottom: 16px;
  }
  .contact-list li::before {
    content: ""; position: absolute; left: 0; top: 6px;
    width: 8px; height: 8px; background: var(--accent);
  }

  /* Brand side */
  .card--brand { top: 660px; background: var(--black); }
  .frame {
    position: absolute; left: 21px; top: 20px; right: 22px; bottom: 22px;
    border: 4px solid var(--accent);
  }
  .pointer { position: absolute; top: 186px; }
  .pointer--left { left: 21px; }
  .pointer--right { right: 22px; }
  .brand-name {
    position: absolute; left: 0; right: 0; top: 184px;
    display: flex; align-items: center; justify-content: center; gap: 14px;
    font-weight: 400; font-size: 31px; letter-spacing: 0.5px;
    color: var(--white); line-height: 1;
  }
  .brand-name__square { width: 14px; height: 14px; background: var(--white); }
</style>
</head>
<body>
<div class="canvas">

  <section class="card card--contact">
    <div class="portrait">
      <div class="portrait__fill" role="img" aria-label="Schwarz-weiß Porträtfoto des Personal Trainers"></div>
    </div>
    <h1 class="name">Tobias Kellinger</h1>
    <p class="website">www.tobiaskellinger.de</p>
    <svg class="divider" width="445" height="8" viewBox="0 0 445 8">
      <polygon points="0,1 445,3 445,4 0,7" fill="var(--accent)"/>
    </svg>
    <ul class="contact-list">
      <li>t.kellinger@postfach.de</li>
      <li>0163/2918374</li>
      <li>Lindenfeldweg 14<br>80412 München</li>
    </ul>
  </section>

  <section class="card card--brand">
    <div class="frame"></div>
    <svg class="pointer pointer--left" width="32" height="32" viewBox="0 0 32 32">
      <polygon points="0,0 32,16 0,32" fill="var(--accent)"/>
    </svg>
    <svg class="pointer pointer--right" width="32" height="32" viewBox="0 0 32 32">
      <polygon points="32,0 0,16 32,32" fill="var(--accent)"/>
    </svg>
    <div class="brand-name">
      <span class="brand-name__square"></span>
      <span>TOBIAS KELLINGER</span>
    </div>
  </section>

</div>
</body>
</html>
```